Rack Card for Portuguese Walking Food Tour

I would like a vertical rack card measuring 99x210mm. Here is the information I would like to include. It does not need to be in this format. We are located in Setubal, Portugal.
Please use the attached Teal Heron Logo.
Setúbal: Tradition and Today
Experience the culinary delights of Setúbal, Portugal with a walking food tour around our waterfront village. Discover the Mercado da Gaivota Branca, voted one of the world’s best markets by Metro Ledger, and indulge in local wines and dishes. Prepare for a calm stroll on flat streets. No hills to climb on this tour.
Duration: 4 hours
www.brinebasketwalks.com
+351 265 000 487

```html
<!DOCTYPE html>
<html lang="en">
<head>
<meta charset="utf-8">
<title>Brine Basket Walks – Rack Card</title>
<link rel="stylesheet" href="https://fonts.googleapis.com/css2?family=Lobster&family=Montserrat:wght@400;700&display=swap">
<style>
  :root {
    --page-bg: #ececec;
    --card-white: #ffffff;
    --brand-orange: #f06a24;
    --title-crimson: #c8194b;
    --ink-black: #0c0c0c;
    --text-white: #ffffff;
  }
  * { box-sizing: border-box; margin: 0; padding: 0; }
  html, body {
    width: 927px; height: 1200px; overflow: hidden;
    background: var(--page-bg);
  }
  .rack-card {
    position: absolute; left: 199px; top: 40px;
    width: 528px; height: 1120px;
    background: var(--card-white);
    overflow: hidden;
    box-shadow: 0 6px 24px rgba(0,0,0,0.18);
  }
  .card-art { position: absolute; inset: 0; }
  .brand {
    position: absolute; left: 52px; top: 70px;
    display: flex; align-items: center; gap: 22px;
  }
  .brand-mark {
    width: 92px; height: 92px; border-radius: 50%;
    background: var(--brand-orange);
    flex: none;
  }
  .brand-name {
    font-family: "Montserrat", sans-serif; font-weight: 700;
    font-size: 34px; line-height: 1.1; color: var(--ink-black);
  }
  .headline {
    position: absolute; left: 0; right: 0; top: 708px;
    text-align: center;
    font-family: "Lobster", cursive; font-weight: 400;
    font-size: 60px; line-height: 1;
    color: var(--title-crimson);
    -webkit-text-stroke: 6px var(--text-white);
    paint-order: stroke fill;
  }
  .intro {
    position: absolute; left: 42px; right: 42px; top: 796px;
    text-align: center;
    font-family: "Montserrat", sans-serif; font-weight: 400;
    font-size: 19px; line-height: 27px;
    color: var(--text-white);
  }
  .contact-bar {
    position: absolute; left: 0; right: 0; bottom: 0; height: 53px;
    background: var(--ink-black);
    display: flex; align-items: center; justify-content: space-between;
    padding: 0 20px 0 22px;
    font-family: "Montserrat", sans-serif; font-weight: 700;
    color: var(--text-white);
  }
  .contact-web { font-size: 14.5px; }
  .contact-phone { font-size: 25px; }
</style>
</head>
<body>
  <article class="rack-card">
    <svg class="card-art" width="528" height="1120" viewBox="0 0 528 1120">
      <defs>
        <clipPath id="collage-shape">
          <path d="M0,334 C150,288 370,282 528,338 L528,604 C420,680 250,694 0,690 Z"/>
        </clipPath>
        <linearGradient id="bar-tones" x1="0" y1="0" x2="0" y2="1">
          <stop offset="0" stop-color="#5a68aa"/>
          <stop offset="0.55" stop-color="#8a7f86"/>
          <stop offset="1" stop-color="#c9a33a"/>
        </linearGradient>
      </defs>
      <path class="orange-field" fill="var(--brand-orange)"
            d="M0,306 C130,232 330,206 528,226 L528,1067 L0,1067 Z"/>
      <g clip-path="url(#collage-shape)">
        <rect x="0" y="270" width="166" height="250" fill="#8d7f93" role="img" aria-label="Photo: heart sign spelling the town's initials in front of the municipal hall"/>
        <rect x="166" y="270" width="150" height="250" fill="#c6976a" role="img" aria-label="Photo: board of sliced sausage, toast and local cheese"/>
        <rect x="0" y="520" width="166" height="180" fill="#b39a80" role="img" aria-label="Photo: market stall with sacks of dried beans and price tags"/>
        <rect x="166" y="520" width="150" height="180" fill="#c8ced2" role="img" aria-label="Photo: fresh oysters on ice with lemon"/>
        <rect x="316" y="270" width="212" height="430" fill="url(#bar-tones)" role="img" aria-label="Photo: glass of beer and sparkling wine at an outdoor café table"/>
      </g>
      <path d="M0,334 C150,288 370,282 528,338" fill="none" stroke="var(--card-white)" stroke-width="8"/>
      <path d="M528,604 C420,680 250,694 0,690" fill="none" stroke="var(--card-white)" stroke-width="8"/>
    </svg>

    <header class="brand">
      <span class="brand-mark"></span>
      <span class="brand-name">Brine Basket<br>Walks</span>
    </header>

    <h1 class="headline">Tradition and Today</h1>

    <p class="intro">Experience the culinary delights of Setúbal, Portugal with a walking food tour around our waterfront village. Discover the Mercado da Gaivota Branca, voted one of the world’s best markets by Metro Ledger, and indulge in local wines and dishes. Prepare for a calm stroll on flat streets. No hills to climb on this tour.</p>

    <footer class="contact-bar">
      <span class="contact-web">www.brinebasketwalks.com</span>
      <span class="contact-phone">+351 265 000 487</span>
    </footer>
  </article>
</body>
</html>
```